Rehabilitation Centre Driving Evaluation brochure

I have already designed a brochure when I was at my previous workplace, but need a new one for my own rehab clinic. I will attach the brochure that I already did, as the information hasn't really changed. It is just very old and very ugly. It is an information pamphlet that will be in physician offices. Please let me know if you need anything else.

Target Market(s)

physicians, rehabilitation professionals, therapists, and individuals with medical conditions who want to return to driving

Industry/Entity Type

Medical

Requirements
Nice to have
• I am not stuck on the trifold, and actually may prefer a single fold brochure.

```html
<!DOCTYPE html>
<html lang="en">
<head>
<meta charset="utf-8">
<title>Driving Evaluation and Training Center – Brochure</title>
<link href="https://fonts.googleapis.com/css2?family=Oswald:wght@700&family=Questrial&display=swap" rel="stylesheet">
<style>
  :root {
    --navy: #17466a;
    --lime: #b8c70e;
    --white: #ffffff;
    --grey: #9a9a9a;
    --photo-dark: #1d2a3d;
    --photo-mid: #3d5577;
    --photo-warm: #a9705a;
  }
  html, body {
    margin: 0;
    padding: 0;
    overflow: hidden;
    background: var(--white);
  }
  .brochure {
    position: relative;
    width: 1200px;
    height: 848px;
    overflow: hidden;
    background: var(--white);
    font-family: "Questrial", "Century Gothic", sans-serif;
  }
  .backdrop {
    position: absolute;
    inset: 0;
  }
  .referral {
    position: absolute;
    left: 180px;
    top: 44px;
    width: 372px;
    color: var(--white);
  }
  .referral h2 {
    margin: 0 0 12px;
    font-weight: 400;
    font-size: 23px;
    letter-spacing: 0.3px;
    color: var(--lime);
  }
  .referral p {
    margin: 0 0 17px;
    font-size: 14.4px;
    line-height: 18px;
    letter-spacing: 0.5px;
  }
  .title {
    position: absolute;
    left: 800px;
    top: 98px;
    margin: 0;
    white-space: nowrap;
    font-family: "Oswald", "League Gothic", sans-serif;
    font-weight: 700;
    font-size: 52px;
    line-height: 51px;
    letter-spacing: -1.5px;
    color: var(--white);
    text-transform: uppercase;
    transform: scaleX(0.88);
    transform-origin: left top;
  }
  .brand {
    position: absolute;
    display: flex;
    align-items: center;
    gap: 12px;
    white-space: nowrap;
    color: var(--navy);
  }
  .brand-dot {
    flex: none;
    border-radius: 50%;
    background: var(--lime);
  }
  .brand-name {
    font-weight: 400;
    line-height: 1.08;
  }
  .brand--back { left: 62px; top: 476px; }
  .brand--back .brand-dot { width: 24px; height: 24px; }
  .brand--back .brand-name { font-size: 27px; }
  .brand--front { left: 636px; top: 508px; }
  .brand--front .brand-dot { width: 30px; height: 30px; }
  .brand--front .brand-name { font-size: 30px; }
  .contact {
    position: absolute;
    left: 116px;
    top: 626px;
    margin: 0;
    padding: 0;
    list-style: none;
    color: #1a1a1a;
    font-size: 16px;
    line-height: 19px;
  }
  .contact li {
    display: flex;
    align-items: flex-start;
    gap: 10px;
    margin-bottom: 8px;
  }
  .contact li.address { margin-bottom: 16px; }
  .contact svg {
    flex: none;
    width: 16px;
    height: 16px;
    margin-top: 1px;
    fill: none;
    stroke: var(--lime);
    stroke-width: 1.6;
  }
  .contact svg .solid { fill: var(--lime); stroke: none; }
  .tagline {
    position: absolute;
    left: 650px;
    top: 698px;
    margin: 0;
    font-size: 22.5px;
    line-height: 27px;
    font-weight: 400;
  }
  .tagline .lead { color: var(--navy); display: block; }
  .tagline .rest { color: var(--lime); display: block; padding-left: 37px; }
  .front-url {
    position: absolute;
    left: 640px;
    top: 794px;
    font-size: 14.5px;
    color: var(--grey);
  }
</style>
</head>
<body>
<div class="brochure">
  <svg class="backdrop" width="1200" height="848" viewBox="0 0 1200 848">
    <defs>
      <linearGradient id="roadGlow" x1="0" y1="0" x2="1" y2="1">
        <stop offset="0" stop-color="#8fa3bf"/>
        <stop offset="0.35" stop-color="#3d5577"/>
        <stop offset="0.6" stop-color="#1d2a3d"/>
        <stop offset="0.8" stop-color="#a9705a"/>
        <stop offset="1" stop-color="#1d2a3d"/>
      </linearGradient>
    </defs>
    <path class="navy-field" fill="var(--navy)" d="M0,0 H1200 V848 H0 Z"/>
    <path class="white-field" fill="var(--white)"
          d="M0,232 C180,370 500,395 756,436 C960,500 1080,660 1114,848 H0 Z"/>
    <path class="street-photo" role="img" aria-label="Photo: close-up of a car's rear light in evening traffic"
          fill="url(#roadGlow)"
          d="M664,0 H1200 V848 H1128 C1100,660 980,500 770,420 C715,310 680,160 664,0 Z"/>
    <path class="stripe-white" fill="var(--white)"
          d="M590,0 H608 C640,180 700,330 770,420 C680,330 620,180 590,0 Z"/>
    <path class="stripe-lime" fill="var(--lime)"
          d="M608,0 H664 C680,160 716,318 770,420 C700,330 640,180 608,0 Z"/>
  </svg>

  <section class="referral">
    <h2>Referral Process</h2>
    <p>Referrals maybe made by physicians, therapists, individuals requiring service, insurance companies, case managers, community service agencies, etc. The referral source will be asked to complete a referral form. The client’s physician will be contacted and asked to complete a medical referral form stating the client is medically able to participate in the assessment.</p>
    <p>Referrals can be made for any individual who requires an evaluation of their driving skills or adaptive equipment needs by contacting us.</p>
  </section>

  <h1 class="title">Driving Evaluation<br>and Training Center</h1>

  <div class="brand brand--back">
    <span class="brand-dot"></span>
    <span class="brand-name">Meridian<br>Rehabilitation<br>Associates</span>
  </div>

  <ul class="contact">
    <li class="address">
      <svg viewBox="0 0 16 16"><path d="M8 15s5-5 5-8.5a5 5 0 0 0-10 0C3 10 8 15 8 15z"/><circle cx="8" cy="6.5" r="1.8"/></svg>
      <span>2480 Alderbrook Road, Unit #4<br>Kingsville, Ontario, N8X 2R5</span>
    </li>
    <li>
      <svg viewBox="0 0 16 16"><path class="solid" d="M3 1.5l2.5-.5 1.5 3.5-1.8 1.2a8 8 0 0 0 4.6 4.6l1.2-1.8 3.5 1.5-.5 2.5c-.3 1-1.3 1.5-2.5 1.3C6.5 12.6 3.4 9.5 2.2 4c-.2-1.2.3-2.2.8-2.5z"/></svg>
      <span>519 555 0142</span>
    </li>
    <li>
      <svg viewBox="0 0 16 16"><rect class="solid" x="4" y="1" width="8" height="4"/><rect class="solid" x="1" y="6" width="14" height="6" rx="1"/><rect x="4.5" y="10" width="7" height="5" fill="#fff"/></svg>
      <span>519 555 0143</span>
    </li>
    <li>
      <svg viewBox="0 0 16 16"><rect x="1.5" y="3.5" width="13" height="9"/><path d="M1.5 3.5l6.5 5.5 6.5-5.5"/></svg>
      <span>office@meridianrehab.ca</span>
    </li>
    <li>
      <svg viewBox="0 0 16 16"><circle cx="8" cy="8" r="6.5"/><ellipse cx="8" cy="8" rx="3" ry="6.5"/><path d="M1.5 8h13M2.5 4.8h11M2.5 11.2h11"/></svg>
      <span>www.meridianrehab.ca</span>
    </li>
  </ul>

  <div class="brand brand--front">
    <span class="brand-dot"></span>
    <span class="brand-name">Meridian<br>Rehabilitation<br>Associates</span>
  </div>

  <p class="tagline">
    <span class="lead">A comprehensive</span>
    <span class="rest">driver rehabilitation program</span>
  </p>

  <div class="front-url">www.meridianrehab.ca</div>
</div>
</body>
</html>
```